Gym Wall Story Feature-- Long Horizontal design for the full-width of the gym wall

We need a horizontal, LONG, story poster/display that artfully tells our gym's story using ALL of the attached information and photographs. I've also included where this display will go in our gym (aligned with, and under the trophies.) Please incorporate the color scheme of white, light grey, dark grey, and orange.

Thanks!

Target Market(s)

Upscale, exclusive, hip gym community

Industry/Entity Type

Gym

Font styles to use
Sans Serif

Colors
ffffff
000000
aaaaaa
5c5c5c
f78f20
e9e9e9

Requirements
Must have
• All images and text provided in the attachments. Clean, modern, design. MOSTLY white with just a couple pops of orange and light grey. text should be black or charcoal and easy to read. We would like to have our logo incorporated as well.
Nice to have
• Clean, stream-line look, nothing too busy or crowded.
Should not have
• Too busy, slanted lines, weird fonts, misalignment.

```html
<!DOCTYPE html>
<html lang="en">
<head>
<meta charset="utf-8">
<title>How Did The Tempo Start?</title>
<link href="https://fonts.googleapis.com/css2?family=Saira+Semi+Condensed:wght@700;800&family=Open+Sans:ital,wght@0,400;0,700;1,700&display=swap" rel="stylesheet">
<style>
  :root {
    --white: #ffffff;
    --black: #000000;
    --grey-light: #e9e9e9;
    --grey-mid: #aaaaaa;
    --charcoal: #5c5c5c;
    --ink: #3d3d3d;
    --orange: #f47a30;
    --orange-soft: #f7b48a;
  }
  * { margin: 0; padding: 0; box-sizing: border-box; }
  html, body { width: 1200px; height: 927px; overflow: hidden; background: var(--white); }
  .poster {
    position: relative; width: 1200px; height: 927px; overflow: hidden;
    background: var(--white);
    font-family: "Open Sans", Arial, sans-serif; color: var(--ink);
  }
  .hero-backdrop {
    position: absolute; inset: 0;
    background:
      radial-gradient(ellipse 520px 360px at 1000px 170px, rgba(244,122,48,.55), rgba(244,122,48,0) 70%),
      radial-gradient(ellipse 380px 260px at 760px 130px, rgba(247,180,138,.45), rgba(255,255,255,0) 70%),
      radial-gradient(ellipse 600px 200px at 600px 900px, rgba(247,180,138,.35), rgba(255,255,255,0) 70%);
  }
  .photo { position: absolute; border: 2px solid var(--orange); }
  .photo-1973 { left: 40px; top: 48px; width: 220px; height: 350px; background: linear-gradient(160deg, #8a8a8a, #3a3a3a); }
  .photo-1981 { left: 40px; top: 510px; width: 219px; height: 348px; background: linear-gradient(160deg, #6a6e78, #a5582c 60%, #3b2a22); }
  .photo-2015 { left: 669px; top: 507px; width: 219px; height: 349px; background: linear-gradient(170deg, #d9d8b0, #9a9a86 45%, #2b2b2b 80%); }
  .year-tag {
    position: absolute; height: 19px; width: 63px;
    background: var(--orange); color: var(--white);
    font-weight: 700; font-size: 13px; letter-spacing: 3px;
    display: flex; align-items: center; justify-content: center;
  }
  .tag-1973 { left: 118px; top: 398px; }
  .tag-1981 { left: 118px; top: 858px; }
  .tag-2015 { left: 747px; top: 857px; }
  .headline {
    position: absolute; left: 290px; top: 46px;
    font-family: "Saira Semi Condensed", Arial, sans-serif; font-weight: 800;
    color: var(--charcoal); line-height: 1; text-transform: uppercase; white-space: nowrap;
  }
  .headline .lead { display: block; font-size: 42px; letter-spacing: 1px; }
  .headline .main { display: block; font-size: 60px; margin-top: 2px; }
  .headline .accent { color: var(--orange); }
  .story {
    position: absolute; font-size: 14.6px; line-height: 21.5px;
    text-align: justify; color: var(--ink);
  }
  .story-origin { left: 290px; top: 161px; width: 441px; }
  .story-method { left: 290px; top: 561px; width: 330px; }
  .quote {
    position: absolute; left: 290px; top: 353px; width: 441px;
    font-style: italic; font-weight: 700; font-size: 14.6px; line-height: 21.5px;
    text-align: justify; color: var(--ink);
  }
  .brand {
    position: absolute; left: 333px; top: 462px;
    display: flex; align-items: center; gap: 10px; white-space: nowrap;
    font-family: "Saira Semi Condensed", Arial, sans-serif; font-weight: 800;
    font-size: 44px; line-height: 1; color: var(--charcoal); text-transform: uppercase;
  }
  .brand-mark { width: 16px; height: 16px; background: var(--orange); flex: none; }
  .titles {
    position: absolute; left: 915px; top: 555px;
    font-family: "Saira Semi Condensed", Arial, sans-serif; font-weight: 800;
    text-transform: uppercase; line-height: 1; white-space: nowrap;
  }
  .titles .big { display: block; font-size: 48px; color: var(--orange); }
  .titles .sub { display: block; font-size: 28px; color: var(--charcoal); margin-top: 3px; }
  .wins { position: absolute; left: 915px; top: 681px; list-style: none; }
  .wins li {
    width: 241px; height: 24px; margin-bottom: 9.5px;
    display: flex; align-items: center; justify-content: center; white-space: nowrap;
    color: var(--white); font-weight: 700; font-size: 14.5px; line-height: 1;
    box-shadow: 0 1px 2px rgba(0,0,0,.25);
  }
  .wins .orange { background: var(--orange); }
  .wins .dark { background: var(--charcoal); }
  .base-band { position: absolute; left: 0; width: 1200px; }
  .band-dark { top: 902px; height: 11px; background: var(--charcoal); }
  .band-orange { top: 913px; height: 14px; background: var(--orange); }
</style>
</head>
<body>
<main class="poster">
  <div class="hero-backdrop" role="img" aria-label="Soft-focus rack of dumbbells glowing in warm orange light"></div>

  <div class="photo photo-1973" role="img" aria-label="Black and white photo of Rowan competing on stage in 1973"></div>
  <span class="year-tag tag-1973">1973</span>

  <h1 class="headline">
    <span class="lead">How did the</span>
    <span class="main">Tempo<span class="accent">Start?</span></span>
  </h1>

  <p class="story story-origin">The Tempo began with body builder and personal trainer, Rowan Calder. Rowan had a passion for fitness early on and opened his first gym in 1960. Shortly after, Rowan won Mr. Blue Ridge. Rowan’s body-building career looked promising until one evening he was robbed and shot in the chest. As a result, Rowan suffered from nerve damage in the arm and figured at the age of 34, his weight lifting days were over.</p>

  <p class="quote">“I thought I was through and couldn’t continue lifting but the tempo changed everything,”</p>

  <div class="brand"><span class="brand-mark"></span>The Tempo</div>

  <div class="photo photo-1981" role="img" aria-label="Colour photo of Rowan posing on stage in 1981"></div>
  <span class="year-tag tag-1981">1981</span>

  <p class="story story-method">Rowan started with 2-pound weights and changed his whole training technique. No more bouncing or slinging, just steady and controlled movements. Through hard work and consistency, Rowan started shaping up his upper-body again. Shortly after turning 40, Rowan won the National Mr. Atlas competition. Through his experiences, Rowan created The Tempo; a system that helps individuals develop a fundamentally sound workout regimen and accountability system.</p>

  <div class="photo photo-2015" role="img" aria-label="Photo of Rowan standing in his training studio in 2015"></div>
  <span class="year-tag tag-2015">2015</span>

  <h2 class="titles">
    <span class="big">National</span>
    <span class="sub">Championships</span>
    <span class="sub">Won:</span>
  </h2>
  <ul class="wins">
    <li class="orange">1981 Won Past 40 Mr. Atlas</li>
    <li class="dark">1996 Won Past 50 Mr. Atlas</li>
    <li class="dark">1999 Won Past 60 Mr. Atlas</li>
    <li class="orange">2009 Won Past 70 Mr. Atlas</li>
  </ul>

  <div class="base-band band-dark"></div>
  <div class="base-band band-orange"></div>
</main>
</body>
</html>
```